Design for Employee Baseball Cards

Looking to design baseball cards for my employees. Trying to replicate famous baseball card design with swapping in an employee and listing there stats and fun facts. These cards will be inserted into boxes so customers can receive with their orders. Cards allow customers to put a face to the name they've always corresponded with, which makes their experience personable and more memorable.

Looking for a front and back design template. We are open to the design, but would like it to resemble a baseball/playing card.
Size: 2.5" x 3.5" vertical
Here is our website which can be referenced for color pallet and tone.
https://www.crateworksdirect.com/

Attached is an example of a vintage baseball. Can we see some versions like this?

Front
- Person's name
- Title/Department
- Crate Works Direct logo
- Person's photo - this will be an action shot like a baseball card

Back
I'm open to the design and content of the back. We want it to resemble a back of a baseball card as best as possible. Normally, baseball cards will have stats by year. Instead, we can have stats and fun facts like the following

Items for Back
- Bio
- Year started at CWD
- Department
- Years of experience
- Specialty
- Secret skill
- What you love about CWD
- Favorite quote
- Fun fact
- Passion outside of CWD
- Person's photo - we can include a smaller headshot

Font styles to use
Sans Serif

Colors
0054AA
0677BA
7BADD7
CADEEF
E8F1F8

Requirements
Must have
• The deliverable must be a template PSD or AI that we can swap in photos and edit text for each person's card.

```html
<!DOCTYPE html>
<html lang="en">
<head>
<meta charset="utf-8">
<title>Employee Trading Card – Front and Back Template</title>
<link href="https://fonts.googleapis.com/css2?family=Arimo:wght@400;700&family=Barlow+Condensed:wght@600;700&family=Luckiest+Guy&family=Montserrat:wght@900&family=Russo+One&display=swap" rel="stylesheet">
<style>
  :root{
    --wood-light:#e6c9a4;
    --wood-dark:#cfa77c;
    --panel-grey:#a6a5a5;
    --panel-light:#dcdcdc;
    --ink:#111111;
    --navy:#34499c;
    --navy-deep:#1d2f73;
    --gold:#c9a033;
    --yellow:#e3c600;
    --card-grey:#e2e2e2;
    --white:#ffffff;
    --photo-light:#eef1f3;
    --photo-mid:#b9c0c6;
    --brand-blue:#5a6f95;
  }
  *{box-sizing:border-box;margin:0;padding:0}
  html,body{width:1200px;height:700px;overflow:hidden;background:var(--panel-light)}
  .canvas{position:relative;width:1200px;height:700px;font-family:Arimo,sans-serif;color:var(--ink)}

  /* ---------- front side ---------- */
  .front-stage{position:absolute;left:0;top:0;width:500px;height:700px;
    background:linear-gradient(100deg,var(--wood-light),var(--wood-dark) 45%,var(--wood-light) 70%,var(--wood-dark))}
  .front-photo{position:absolute;left:30px;top:28px;width:440px;height:590px;
    background:linear-gradient(160deg,var(--photo-light),var(--photo-mid) 60%,#6d7177);
    border:3px solid var(--ink);
    clip-path:polygon(0 0,100% 0,100% 85%,87% 100%,0 100%)}
  .front-logo{position:absolute;left:30px;top:25px;width:116px;height:116px;border-radius:50%;
    background:var(--white);border:3px solid var(--ink);display:flex;align-items:center;justify-content:center;
    text-align:center;font:700 14px/1.1 Arimo,sans-serif;color:var(--navy-deep)}
  .name-plate{position:absolute;left:143px;top:600px;width:327px;height:71px;background:var(--gold);
    border:3px solid var(--ink);display:flex;align-items:center;justify-content:center;text-align:center;
    font:32px/0.85 "Luckiest Guy",sans-serif;letter-spacing:4px;color:var(--ink)}
  .front-brand{position:absolute;left:50px;top:632px;width:90px;color:var(--brand-blue);
    font:400 17px/0.95 Arimo,sans-serif}
  .front-brand small{display:block;font-size:4px;margin-top:3px;color:#8a8a8a}

  /* ---------- labels ---------- */
  .label-band{position:absolute;left:500px;top:0;width:700px;height:200px;background:var(--panel-grey)}
  .side-label{position:absolute;font:900 38px/1 Montserrat,sans-serif;letter-spacing:9px;color:var(--ink)}
  .side-label.front{left:518px;top:30px}
  .side-label.back{left:783px;top:130px}
  .back-chevron{position:absolute;left:838px;top:170px}

  /* ---------- back side ---------- */
  .back-card{position:absolute;left:0;top:0;width:1200px;height:700px}
  .card-number{position:absolute;left:541px;top:230px;width:58px;height:37px;background:var(--yellow);
    font:400 26px/37px "Russo One",sans-serif;text-align:center;color:var(--ink)}
  .player-title{position:absolute;left:695px;top:226px;font:400 40px/45px "Russo One",sans-serif;color:var(--white)}
  .player-title span{font-size:24px}
  .bio-top{position:absolute;left:524px;top:281px;width:461px;height:22px;background:var(--card-grey);
    font-size:14.5px;line-height:22px;padding-left:41px;white-space:pre}
  .stat-panel{position:absolute;left:524px;top:303px;width:461px;height:116px;background:var(--yellow)}
  .stat{position:absolute;top:6px;text-align:center;font:700 21px/28px Arimo,sans-serif}
  .stat.exp{left:85px;width:160px}
  .stat.start{left:210px;width:190px}
  .stat-rule{position:absolute;left:16px;right:14px;top:60px;border-top:2px solid var(--ink)}
  .love{position:absolute;left:0;right:0;top:67px;text-align:center;font-size:14px;line-height:15.5px}
  .love b{font:700 13.5px Barlow Condensed,sans-serif;letter-spacing:.2px}
  .bio-body{position:absolute;left:524px;top:419px;width:461px;height:200px;background:var(--card-grey)}
  .bio-text{position:absolute;left:0;width:461px;top:5px;text-align:center;font-size:13.4px;line-height:16.5px}
  .facts{position:absolute;left:529px;top:478px;width:449px;border-collapse:collapse;font-size:13.5px}
  .facts td{border-top:1.5px solid var(--ink);height:23px;vertical-align:middle;padding:0 3px;line-height:14px}
  .facts th{border-top:1.5px solid var(--ink);border-right:1.5px solid var(--ink);width:108px;text-align:right;
    padding-right:3px;font:700 14px Barlow Condensed,sans-serif;vertical-align:middle;white-space:nowrap}
  .facts tr.quote th,.facts tr.quote td{vertical-align:top;padding-top:5px;height:60px}
  .headshot{position:absolute;left:986px;top:281px;width:192px;height:338px;
    background:linear-gradient(180deg,#d9dde0,#b9bec3 45%,#3a3d44)}
  .foot-name{position:absolute;left:686px;top:634px;font:700 23px/1 "Barlow Condensed",sans-serif;color:var(--ink)}
  .foot-legal{position:absolute;left:686px;top:662px;font:700 8.5px/1 Arimo,sans-serif}
  .foot-contact{position:absolute;right:125px;top:634px;text-align:right;font:700 12px/11.5px "Barlow Condensed",sans-serif}
  .foot-contact .site{font-size:13px}
  .foot-mark{position:absolute;left:1104px;top:640px;font:700 13px/1 "Barlow Condensed",sans-serif;color:var(--white)}
</style>
</head>
<body>
<div class="canvas">

  <!-- front of card -->
  <section class="front-stage" aria-label="Card front">
    <div class="front-photo" role="img" aria-label="Action photo of the employee"></div>
    <div class="front-logo">Crate<br>Works<br>Direct</div>
    <div class="name-plate">JOHN<br>SMITH</div>
    <div class="front-brand">Crate Works Direct<small>Solutions that enhance your brand</small></div>
  </section>

  <!-- presentation labels -->
  <div class="label-band"></div>
  <div class="side-label front">&lt;&nbsp;FRONT</div>
  <div class="side-label back">BACK</div>
  <svg class="back-chevron" width="24" height="18" viewBox="0 0 24 18"><path d="M2 2 L12 15 L22 2" fill="none" stroke="#111" stroke-width="5"/></svg>

  <!-- back of card -->
  <section class="back-card" aria-label="Card back">
    <svg width="1200" height="700" style="position:absolute;left:0;top:0">
      <polygon points="523,248 547,225 1150,225 1179,248 1150,271 547,271" fill="var(--navy)"/>
      <polygon points="528,248 549,229 1148,229 1170,248 1148,268 549,268" fill="none" stroke="var(--navy-deep)" stroke-width="1.5"/>
      <polygon points="523,281 532,280 1170,280 1180,290 1180,610 1170,620 532,620 523,611" fill="var(--card-grey)" stroke="var(--ink)" stroke-width="3"/>
      <polygon points="522,258 546,278 522,292" fill="var(--yellow)" stroke="var(--ink)" stroke-width="1.5"/>
      <polygon points="1180,258 1156,278 1180,292" fill="var(--yellow)" stroke="var(--ink)" stroke-width="1.5"/>
      <polygon points="522,608 546,628 522,642" fill="var(--yellow)" stroke="var(--ink)" stroke-width="1.5"/>
      <polygon points="1180,608 1156,628 1180,642" fill="var(--yellow)" stroke="var(--ink)" stroke-width="1.5"/>
      <polygon points="523,653 547,630 1150,630 1179,653 1150,677 547,677" fill="var(--navy)"/>
      <rect x="560" y="633" width="527" height="40" fill="var(--yellow)"/>
      <circle cx="576" cy="653" r="17" fill="var(--navy)"/>
      <circle cx="619" cy="653" r="17" fill="var(--navy)"/>
      <circle cx="661" cy="653" r="17" fill="var(--navy)"/>
    </svg>

    <div class="card-number">001</div>
    <div class="player-title">FIRST LAST <span>• DEPARTMENT</span></div>

    <div class="bio-top">Hometown: Mahwah, NJ   |   Bats: Left   Throws: Right</div>
    <div class="stat-panel">
      <div class="stat exp">Years Exp.<br>17</div>
      <div class="stat start">Started at CWD<br>2007</div>
      <div class="stat-rule"></div>
      <p class="love"><b>WHAT YOU LOVE ABOUT WORKING AT CWD:</b><br>Challenging work and great people!<br>(Extra line for more information)</p>
    </div>

    <div class="bio-body">
      <p class="bio-text">THE 2ND HIGHEST ALL-STAR VOTE-GETTER FOR THE AL IN ‘91, AND<br>THE FIRST HARBOR HAWK VOTED INTO AN ALL-STAR GAME,<br>HAS 2 CAREER PH, BOTH GAME-WINNING HOME RUNS.</p>
    </div>
    <table class="facts">
      <tr><th>SPECIALTY:</th><td>Customer Service &amp; Copier Repair</td></tr>
      <tr><th>OUTSIDE PASSION:</th><td>Finding the best cheesesteak in NJ</td></tr>
      <tr><th>FUN FACT:</th><td>Hums Star-Spangled Banner in 6 languages</td></tr>
      <tr><th>SECRET SKILL:</th><td>Plays guitar like Rex Calloway</td></tr>
      <tr class="quote"><th>FAVORITE QUOTE:</th><td>“You better cut the pizza in four pieces because I’m not hungry enough to eat six.”  -Hal Dorsey</td></tr>
    </table>

    <div class="headshot" role="img" aria-label="Headshot photo of the employee"></div>

    <div class="foot-name">CrateWorksDirect</div>
    <div class="foot-legal">© 2024 CRATE WORKS DIRECT &nbsp;&nbsp; PRINTED IN USA</div>
    <div class="foot-contact">PHONE<br>EMAIL<br><span class="site">crateworksdirect.com</span></div>
    <div class="foot-mark">CWD</div>
  </section>

</div>
</body>
</html>
```